We need a card and logo design for a new business based in Dallas Texas called Ashgrove Financial LLC.

We provide bridge loans.We offer pay day loans,title loans and check cashing.Our products are emmergency loans that help borrowers meet short term liquidity needs until the next pay check.

The final design should communicate,professionalism,Sophistication and friendliness to our customers.Use the color Blue as much as possible and another eye catching color if possible.We will consider a profesional looking knight logo with the color Blue in it.Please design a full corporate identity.

```html
<!DOCTYPE html>
<html lang="en">
<head>
<meta charset="utf-8">
<title>Ashgrove Financial LLC — Business Card</title>
<link rel="stylesheet" href="https://fonts.googleapis.com/css2?family=Montserrat:wght@700&family=Open+Sans:wght@400;600&family=Yellowtail&display=swap">
<style>
  :root {
    --backdrop: #3a3532;
    --card-white: #ffffff;
    --navy: #2b2a78;
    --ink: #1a1a1a;
    --divider: #9a9a9a;
    --back-center: #4a4d50;
    --back-edge: #141516;
    --on-dark: #ffffff;
  }
  * { box-sizing: border-box; margin: 0; padding: 0; }
  html, body {
    width: 1000px; height: 1200px; overflow: hidden;
    background: var(--backdrop);
  }
  .canvas { position: relative; width: 1000px; height: 1200px; }

  .card {
    position: absolute;
    width: 723px; height: 422px;
    box-shadow: 0 6px 14px rgba(0,0,0,0.45);
  }

  /* Front */
  .card-front { left: 140px; top: 119px; background: var(--card-white); }
  .holder {
    position: absolute; right: 35px; top: 54px; text-align: right;
  }
  .holder-name {
    font-family: "Montserrat", sans-serif; font-weight: 700;
    font-size: 18px; letter-spacing: 1.5px; color: var(--navy);
  }
  .holder-role {
    font-family: "Open Sans", sans-serif; font-size: 15px; color: var(--ink);
    margin-top: 1px;
  }
  .brand {
    position: absolute; left: 0; right: 0; top: 150px;
    display: flex; align-items: center; justify-content: center; gap: 14px;
    font-family: "Montserrat", sans-serif; font-weight: 700;
    font-size: 30px; letter-spacing: 1px;
  }
  .brand-dot { width: 18px; height: 18px; border-radius: 50%; }
  .card-front .brand { color: var(--navy); }
  .card-front .brand-dot { background: var(--navy); }

  .contact {
    position: absolute; top: 312px; left: 35px; right: 35px;
    display: flex;
    font-family: "Open Sans", sans-serif; font-size: 15px; color: var(--ink);
  }
  .contact-col { line-height: 27px; }
  .contact-col.primary { width: 327px; }
  .contact-col.secondary {
    border-left: 1px solid var(--divider);
    padding-left: 18px; height: 77px;
  }
  .contact dt { display: inline; font-weight: 600; color: var(--navy); }
  .contact dd { display: inline; }
  .contact .line { display: block; margin-bottom: -4px; }
  .address-rest { display: block; padding-left: 71px; line-height: 22px; }

  /* Back */
  .card-back {
    left: 125px; top: 638px;
    background: radial-gradient(ellipse at 50% 42%, var(--back-center) 0%, #2c2e30 45%, var(--back-edge) 85%);
  }
  .card-back .brand { top: 140px; color: var(--on-dark); }
  .card-back .brand-dot { background: var(--on-dark); }
  .tagline {
    position: absolute; left: 0; right: 0; top: 252px; text-align: center;
    font-family: "Yellowtail", cursive; font-size: 29px; line-height: 36px;
    color: var(--on-dark);
  }
</style>
</head>
<body>
<main class="canvas">
  <section class="card card-front" aria-label="Card front">
    <div class="holder">
      <div class="holder-name">DANIEL REYES</div>
      <div class="holder-role">Financial Advisor</div>
    </div>
    <div class="brand"><span class="brand-dot"></span>ASHGROVE FINANCIAL LLC</div>
    <dl class="contact">
      <div class="contact-col primary">
        <span class="line"><dt>Tel:</dt> <dd>111-123-4567</dd></span>
        <span class="line"><dt>Email:</dt> <dd>info@ashgrovefinancial.com</dd></span>
      </div>
      <div class="contact-col secondary">
        <span class="line"><dt>Fax:</dt> <dd>111-123-4567</dd></span>
        <span class="line"><dt>Address:</dt> <dd>XXX Some Street Address</dd></span>
        <span class="address-rest">State, Country</span>
      </div>
    </dl>
  </section>

  <section class="card card-back" aria-label="Card back">
    <div class="brand"><span class="brand-dot"></span>ASHGROVE FINANCIAL LLC</div>
    <p class="tagline">Whenever you want an emmergency loan,<br>think Ashgrove Financial LLC!</p>
  </section>
</main>
</body>
</html>
```